Bright Fern Property Services

Design a billboard with our logo that includes bullet points for
Property Maintenance, Plumbing, and Electrical, licensed and insured.
Phone number 865 471 3908

also add the website brightfernps-example.com

```html
<!DOCTYPE html>
<html lang="en">
<head>
<meta charset="utf-8">
<title>Bright Fern Property Services – Billboard</title>
<link href="https://fonts.googleapis.com/css2?family=Abril+Fatface&family=Oswald:wght@400;500;600&display=swap" rel="stylesheet">
<style>
  :root {
    --page: #000000;
    --board: #e1dbd4;
    --forest: #00301a;
    --fern: #2bb24c;
    --mint: #2fbf73;
    --ink: #111111;
    --bracket: #3a3a3a;
    --white: #ffffff;
  }
  * { box-sizing: border-box; margin: 0; padding: 0; }
  html, body { width: 930px; height: 1200px; overflow: hidden; background: var(--page); }
  .billboard {
    position: absolute; left: 30px; top: 397px;
    width: 870px; height: 406px;
    background: var(--board); overflow: hidden;
  }
  .billboard__band {
    position: absolute; left: 0; right: 0; top: 305px; bottom: 0;
    background: var(--forest);
  }
  .billboard__frame {
    position: absolute; inset: 14px;
    border: 1.5px solid var(--mint);
  }
  .billboard__ornaments { position: absolute; inset: 0; }
  .brand {
    position: absolute; top: 44px; left: 0; right: 0;
    text-align: center; color: var(--fern);
    font-family: 'Oswald', sans-serif; font-weight: 500;
    line-height: 1;
  }
  .brand__name { font-size: 36px; letter-spacing: 1px; }
  .brand__sub { font-size: 14px; letter-spacing: 3px; margin-top: 4px; }
  .kicker {
    position: absolute; top: 132px; left: 0; right: 0;
    display: flex; justify-content: center; align-items: center; gap: 20px;
    font-family: 'Oswald', sans-serif; font-weight: 500; font-size: 22px;
    letter-spacing: 26px; color: var(--ink);
  }
  .kicker__dots { width: 96px; height: 8px; }
  .rule { position: absolute; left: 88px; right: 100px; height: 2px; background: var(--ink); }
  .rule--top { top: 160px; }
  .rule--bottom { top: 251px; }
  .headline {
    position: absolute; top: 156px; left: 0; right: 0; text-align: center;
    font-family: 'Abril Fatface', serif; font-size: 86px; line-height: 1;
    color: var(--ink); letter-spacing: -1px;
    text-shadow: 4px 2px 0 var(--board), 6px 4px 0 var(--mint);
  }
  .services {
    position: absolute; top: 254px; left: 86px; right: 88px;
    display: flex; justify-content: space-between; align-items: center;
    font-family: 'Oswald', sans-serif; font-weight: 500; font-size: 32px;
    color: var(--ink); line-height: 1.2;
  }
  .services__sep { width: 42px; height: 12px; }
  .tool-art {
    position: absolute; background: linear-gradient(135deg, #d9d9d9, #8d8d8d);
    border-radius: 6px; opacity: .85;
  }
  .tool-art--wrenches { left: 122px; top: 300px; width: 116px; height: 50px; }
  .tool-art--driver-hammer { left: 596px; top: 292px; width: 96px; height: 76px; }
  .contact {
    position: absolute; top: 312px; left: 260px; width: 330px;
    display: flex; flex-direction: column; align-items: center; gap: 4px;
    font-family: 'Oswald', sans-serif; color: var(--white); line-height: 1;
  }
  .contact__line { display: flex; align-items: center; gap: 8px; font-weight: 500; font-size: 44px; }
  .contact__icon { width: 42px; height: 48px; }
  .contact__web { font-weight: 400; font-size: 17px; letter-spacing: 1px; }
</style>
</head>
<body>
  <section class="billboard" aria-label="Bright Fern Property Services billboard">
    <div class="billboard__band"></div>
    <div class="billboard__frame"></div>

    <svg class="billboard__ornaments" width="870" height="406" viewBox="0 0 870 406" fill="none" stroke="var(--bracket)" stroke-width="2">
      <path d="M70 40 H48 V68"/>
      <path d="M800 40 H822 V68"/>
      <path d="M48 334 V362 H70" stroke="#5a6b60"/>
      <path d="M822 334 V362 H800" stroke="#5a6b60"/>
      <path d="M36 105 V225" stroke="var(--mint)" stroke-width="1.5"/>
      <path d="M834 105 V225" stroke="var(--mint)" stroke-width="1.5"/>
      <path d="M56 297 H100" stroke="var(--mint)" stroke-width="1.5"/>
      <path d="M770 297 H814" stroke="var(--mint)" stroke-width="1.5"/>
    </svg>

    <div class="brand">
      <div class="brand__name">BRIGHT FERN</div>
      <div class="brand__sub">PROPERTY SERVICES LLC</div>
    </div>

    <div class="kicker">
      <svg class="kicker__dots" viewBox="0 0 96 8"><g fill="var(--ink)"><circle cx="4" cy="4" r="1"/><circle cx="14" cy="4" r="1.3"/><circle cx="24" cy="4" r="1.6"/><circle cx="35" cy="4" r="1.9"/><circle cx="47" cy="4" r="2.2"/><circle cx="59" cy="4" r="2.5"/><circle cx="72" cy="4" r="2.8"/><circle cx="86" cy="4" r="3.2"/></g></svg>
      <span>PROPERTY</span>
      <svg class="kicker__dots" viewBox="0 0 96 8"><g fill="var(--ink)"><circle cx="10" cy="4" r="3.2"/><circle cx="24" cy="4" r="2.8"/><circle cx="37" cy="4" r="2.5"/><circle cx="49" cy="4" r="2.2"/><circle cx="61" cy="4" r="1.9"/><circle cx="72" cy="4" r="1.6"/><circle cx="82" cy="4" r="1.3"/><circle cx="92" cy="4" r="1"/></g></svg>
    </div>

    <div class="rule rule--top"></div>
    <h1 class="headline">MAINTENANCE</h1>
    <div class="rule rule--bottom"></div>

    <div class="services">
      <span>PLUMBING</span>
      <svg class="services__sep" viewBox="0 0 42 12" stroke="var(--ink)" stroke-width="2"><path d="M0 2H42M0 6H42M0 10H42"/></svg>
      <span>LICENSED AND INSURED</span>
      <svg class="services__sep" viewBox="0 0 42 12" stroke="var(--ink)" stroke-width="2"><path d="M0 2H42M0 6H42M0 10H42"/></svg>
      <span>ELECTRICAL</span>
    </div>

    <div class="tool-art tool-art--wrenches" role="img" aria-label="Illustration of two wrenches"></div>
    <div class="tool-art tool-art--driver-hammer" role="img" aria-label="Illustration of a screwdriver and hammer"></div>

    <div class="contact">
      <div class="contact__line">
        <svg class="contact__icon" viewBox="0 0 24 24" aria-hidden="true"><path fill="var(--mint)" d="M6.6 2.5c.6-.3 1.3 0 1.6.6l1.8 3.8c.3.6.1 1.3-.4 1.7L8 9.8c.9 2.4 2.9 4.7 5.2 6l1.3-1.5c.5-.5 1.2-.6 1.8-.3l3.6 2c.6.3.8 1 .6 1.6l-.9 2.5c-.3.8-1.1 1.3-2 1.2C9.7 20.6 3.4 13.6 3.6 5.6c0-.8.5-1.6 1.3-1.9z"/></svg>
        <span class="contact__phone">865 471 3908</span>
      </div>
      <span class="contact__web">brightfernps-example.com</span>
    </div>
  </section>
</body>
</html>
```